Inspirational Quote Poster for Employees

For this project, we need a simple yet high-impact poster template that will be customized for each of our employees with a personalized inspirational quote and color scheme. This template should allow us to quickly and easily customize the text and colors in the poster without a lot of effort.

The poster design should consist of:
- A stylized text area to contain the main text of the quote
- A separate text area to contain the source of quote
- A background that complements the color and style of the text

Text may use different typographic effects (such as color, stroke weight, italicization, font size changes, drop shadows) to draw attention to words in the quote; the source of the quote may be formatted the same as the main text of the quote, or may be formatted differently to distinguish it from the main quote.

The background may be simply a single color, subtle texture, gradients, halftone effects, or other color/texture effects may be used to complement the text.

Examples of the types of posters envisioned by this project:
- http://www.pinvelora.example/marcusdtelford/quillbase-job-1/

Sample quotes to use to build your poster - choose whichever one you want, but be certain that the poster design will handle both long and short quotes:
- "Happiness in intelligent people is the rarest thing I know" - Walden Prosket
- "Wanting to be someone else is a waste of the person you are." - Rolf Dintey
- "Experience is not what happens to you. It is what you do with what happens to you." - Ferris Mundell
- "Simplicity is the ultimate in sophistication." - Rinaldo de Pavesco
- "You will get all you want in life if you help enough other people get what they want." - Tad Pomfrey
- "Hell, there are no rules here — we're trying to accomplish something." - Gareth Vullane

Industry/Entity Type

Quote

Requirements
Must have
• Final deliverable must be:
• - Formatted for an 18” x 24” poster (in portrait orientation)
• - Delivered in Adobe InDesign, Adobe Illustrator, or Extended PostScript format
• - Use CMYK color mode
• - Be print-ready at 300dpi resolution
• - Include any fonts used in the template

```html
<!DOCTYPE html>
<html lang="en">
<head>
<meta charset="utf-8">
<title>Quote Poster – Rolf Dintey</title>
<link rel="stylesheet" href="https://fonts.googleapis.com/css2?family=Libre+Baskerville:wght@700&display=swap">
<style>
  :root {
    --bg-deep: #173f8f;
    --bg-mid: #2459b4;
    --bg-light: #3470c8;
    --portrait-warm: #b07a52;
    --portrait-light: #e3c27e;
    --portrait-dark: #3a2a22;
    --text-main: #ffffff;
  }
  html, body {
    margin: 0;
    padding: 0;
    width: 848px;
    height: 1200px;
    overflow: hidden;
  }
  .poster {
    position: relative;
    width: 848px;
    height: 1200px;
    background:
      radial-gradient(ellipse at 50% 40%, var(--bg-light) 0%, var(--bg-mid) 45%, var(--bg-deep) 100%);
    font-family: "Libre Baskerville", Georgia, serif;
    color: var(--text-main);
    overflow: hidden;
  }
  .portrait {
    position: absolute;
    left: 128px;
    top: 62px;
    width: 577px;
    height: 577px;
    border-radius: 50%;
    background:
      radial-gradient(circle at 52% 42%, var(--portrait-warm) 0%, #8a5a3c 40%, transparent 70%),
      linear-gradient(115deg, var(--portrait-light) 0%, #9c7448 35%, var(--portrait-dark) 80%, #25324f 100%);
  }
  .quote {
    position: absolute;
    left: 0;
    right: 0;
    top: 672px;
    margin: 0;
    text-align: center;
    font-size: 58px;
    font-weight: 700;
    line-height: 68px;
    letter-spacing: 0.5px;
  }
  .quote-source {
    position: absolute;
    left: 0;
    right: 0;
    top: 1112px;
    margin: 0;
    text-align: center;
    font-size: 30px;
    font-weight: 700;
    letter-spacing: 0.5px;
  }
</style>
</head>
<body>
  <main class="poster">
    <div class="portrait" role="img" aria-label="Circular portrait photograph of the quote's author"></div>
    <p class="quote">Wanting to be<br>someone else<br>is a waste<br>of the person<br>you are</p>
    <p class="quote-source">- by Rolf Dintey</p>
  </main>
</body>
</html>
```